Simple and clean webdesign for personal homepage

Trying to create a simple and clean webdesign for my personal homepage. Going to use a static site builder with templates to build the site. I want it to have multiple pages - like an about me, blog and resume. I just need something very basic I can customize. I want the main colors to be purple, black and white. I am open to other color palettes too but since purple is my favorite color I want that to be one of the main colors.

The site be mostly text driven. Might have some images in the body text but I want the site design to be light and lean.

Industry/Entity Type

Personal Homepage.

Coding

Coded - Design and coding required

Number of Pages Required

1 page

Font styles to use
Sans Serif

Colors
6B429C
8869AF
B7A5CE
E3DAEB
F3F0F8

Requirements
Must have
• Clean design. Purple used as a color. HTML template.
Nice to have
• Responsive

```html
<!DOCTYPE html>
<html lang="en">
<head>
<meta charset="utf-8">
<title>Daniel Reyes — Web Designer</title>
<link href="https://fonts.googleapis.com/css2?family=Poppins:wght@300;400;500;600&display=swap" rel="stylesheet">
<style>
:root{
  --purple:#6B429C;
  --purple-mid:#8869AF;
  --purple-soft:#B7A5CE;
  --purple-pale:#E3DAEB;
  --purple-mist:#F3F0F8;
  --ink:#222;
  --text:#555;
  --grey-bg:#f7f7f9;
  --line:#e5e5e5;
}
*{box-sizing:border-box;margin:0;padding:0}
html,body{width:1200px;height:4451px;overflow:hidden}
body{font-family:'Poppins',sans-serif;color:var(--text);background:#fff;position:relative}
.abs{position:absolute}
.sec-title{position:absolute;left:0;width:1200px;text-align:center;font-size:30px;font-weight:500;color:var(--ink)}
.sec-title span{color:var(--purple)}
.sec-title::after{content:"";display:block;width:54px;height:3px;background:var(--ink);margin:12px auto 0}
.sec-title.plain::after{display:none}
.btn{position:absolute;background:var(--purple);color:#fff;font-size:13px;display:flex;align-items:center;justify-content:center;border-radius:2px}

/* hero */
.hero{left:0;top:0;width:1200px;height:465px;background:linear-gradient(180deg,#7a52b0 0%,#6a45a2 60%,#7750ad 100%)}
.skyline{left:560px;top:20px;width:640px;height:445px;background:linear-gradient(90deg,rgba(255,255,255,0),rgba(255,255,255,.08) 40%,rgba(255,255,255,.12));}
.brand{left:163px;top:26px;color:#fff}
.brand b{display:block;font-size:34px;font-weight:400;line-height:1}
.brand small{font-size:10px;letter-spacing:3px;font-weight:300}
.nav{left:535px;top:36px;display:flex;gap:54px;font-size:13px;color:#fff}
.nav .on{font-weight:600}
.nav-rule{left:0;top:96px;width:1200px;height:1px;background:rgba(255,255,255,.35)}
.nav-under{left:516px;top:95px;width:70px;height:3px;background:#fff}
.hello{left:532px;top:196px;width:136px;height:48px;background:var(--purple-pale);color:var(--purple);font-size:26px;display:flex;align-items:center;justify-content:center;border-radius:3px}
.hero h1{left:0;top:252px;width:1200px;text-align:center;color:#fff;font-size:46px;font-weight:300}
.hero h1 b{font-weight:600}
.hero p{left:260px;top:324px;width:680px;text-align:center;color:#eee;font-size:14px;line-height:26px}

/* about */
.about-lead{left:163px;top:640px;width:500px;color:var(--purple);font-size:27px;font-weight:300;line-height:43px}
.about-text{left:163px;top:732px;width:500px;font-size:13px;line-height:25px}
.info{left:764px;top:640px;width:272px;font-size:12.5px}
.info div{padding:10px 0 12px;border-bottom:1px solid var(--line);line-height:26px}
.info div b{color:var(--ink);font-weight:500}
.info div:last-child{border:none}
.dl{left:764px;top:813px;width:180px;height:43px}
.stats{left:163px;top:914px;width:874px;display:flex}
.stat{flex:1;text-align:center;border-left:1px solid var(--line);height:106px;padding-top:8px}
.stat:first-child{border:none}
.stat b{display:block;font-size:48px;font-weight:400;color:var(--ink);line-height:56px}
.stat span{font-size:16px;color:var(--ink)}

/* experience */
.exp-bg{left:0;top:1108px;width:1200px;height:778px;background:var(--grey-bg)}
.exp-col{width:360px}
.exp-col::before{content:"";position:absolute;left:0;top:20px;width:1px;height:480px;background:#d5d5d5}
.ex{position:absolute;left:0;width:340px}
.ex i{position:absolute;left:-20px;top:0;width:40px;height:40px;border-radius:50%;background:var(--purple);display:flex;align-items:center;justify-content:center}
.ex .yr{position:absolute;left:35px;top:-2px;color:var(--purple);font-size:14px;font-weight:500;white-space:nowrap;line-height:20px}
.ex h4{position:absolute;left:35px;top:24px;color:var(--ink);font-size:16px;font-weight:500;white-space:nowrap;line-height:22px}
.ex p{position:absolute;left:35px;top:52px;width:300px;font-size:12.5px;line-height:20px}

/* education */
.edu-band{left:0;top:1886px;width:1200px;height:267px;background:var(--purple)}
.edu-title{left:0;top:1970px;width:1200px;text-align:center;color:#fff;font-size:29px;font-weight:500}
.edu-title::after{content:"";display:block;width:54px;height:3px;background:#fff;margin:10px auto 0}
.card{position:absolute;top:2047px;width:204px;height:201px;background:#fff;box-shadow:0 4px 18px rgba(0,0,0,.1);border-radius:3px;text-align:center}
.card .badge{width:100px;height:100px;margin:26px auto 0;border-radius:50%;background:var(--purple-pale)}
.card span{display:block;margin-top:22px;color:var(--purple);font-size:16px}

/* work */
.tile{position:absolute;width:204px;height:203px}
.big{left:724px;top:2427px;width:429px;height:428px;background:linear-gradient(135deg,#27d5ea,#14b8d8)}
.big div{position:absolute;left:16px;top:77px;width:397px;height:257px;border-radius:8px;background:linear-gradient(135deg,#3a1460,#7a2090)}

/* blog */
.blog-bg{left:0;top:3029px;width:1200px;height:768px;background:var(--grey-bg)}
.post{position:absolute;background:#fff;box-shadow:0 3px 14px rgba(0,0,0,.07)}
.post h3{color:var(--ink);font-weight:400;font-size:19px;line-height:30px}
.post p{font-size:10.5px;line-height:21px;color:#333}

/* contact */
.contact-p{left:235px;top:3950px;width:730px;text-align:center;font-size:12.5px;line-height:21px}
.field{position:absolute;border:1px solid #bbb;font-size:12px;color:#999;padding:9px 14px}
.send{left:195px;top:4286px;width:457px;height:35px;background:linear-gradient(90deg,#6B429C,#8869AF);font-size:14px}
.icard{left:702px;top:4013px;width:297px;height:311px;border-radius:8px;background:linear-gradient(160deg,#7a50b0,#8869AF);color:#fff}
.irow{position:absolute;left:30px;display:flex;gap:16px;font-size:14.5px;line-height:20px}
.irow i{width:32px;height:32px;border-radius:50%;background:#fff;flex:none;display:flex;align-items:center;justify-content:center}
.irow b{font-weight:500}

/* footer */
.foot-line{left:0;top:4393px;width:1200px;height:1px;background:var(--line)}
.copy{left:163px;top:4419px;font-size:13px;color:var(--ink)}
.copy b{color:var(--purple);font-weight:500}
.social{left:885px;top:4416px;display:flex;gap:6px}
.social i{width:27px;height:27px;border-radius:50%;border:1.5px solid #333}
.social i.on{background:var(--purple);border-color:var(--purple)}
</style>
</head>
<body>

<section class="abs hero" aria-label="Introduction">
  <div class="abs skyline" role="img" aria-label="Purple-toned city skyline photograph"></div>
  <div class="abs brand"><b>DR</b><small>DANIEL REYES</small></div>
  <nav class="abs nav"><span class="on">HOME</span><span>ABOUT ME</span><span>BLOG</span><span>RESUME</span><span>CONTACT ME</span></nav>
  <div class="abs nav-rule"></div>
  <div class="abs nav-under"></div>
  <div class="abs hello">HELLO !</div>
  <h1 class="abs"><b>I Am</b> Web Designer |</h1>
  <p class="abs">Lorem ipsum dolor sit amet, consectetuer adipiscing elit, sed diam nonummy nibh euismod tincidunt ut laoreet dolore magna aliquam erat volutpat. Ut wisi enim ad minim.</p>
</section>

<h2 class="sec-title" style="top:548px"><span>About</span> Me</h2>
<p class="abs about-lead">I'm Professional We Designer Having 10 Years of Experience</p>
<p class="abs about-text">Lorem ipsum dolor sit amet, consectetuer adipiscing elit, sed diam nonummy nibh euismod tincidunt ut laoreet dolore magna aliquam erat volutpat. Ut wisi enim ad minim veniam, quis nostrud exerci tation ullamcorper suscipit lobortis nisl ut aliquip ex ea commodo consequat. Duis autem vel eum iriure dolor in hendrerit in vulputate.</p>
<div class="abs info">
  <div><b>Name:</b> Daniel Reyes</div>
  <div><b>Email:</b> info@danielreyes.com</div>
  <div><b>Address:</b> 123 Building Name, street Name, City Name, Country - 12345</div>
</div>
<div class="btn dl">&#9113;&nbsp; Download Resume</div>
<div class="abs stats">
  <div class="stat"><b>10+</b><span>Years Experiance</span></div>
  <div class="stat"><b>219+</b><span>Happy Clients</span></div>
  <div class="stat"><b>540+</b><span>Projects Done</span></div>
  <div class="stat"><b>28</b><span>Get Awards</span></div>
</div>

<div class="abs exp-bg"></div>
<h2 class="sec-title plain" style="top:1196px;font-size:30px"><span>Professional Experience</span> &amp; Accomplishments</h2>
<svg width="0" height="0" style="position:absolute"><defs><symbol id="edit" viewBox="0 0 16 16"><rect x="2" y="3" width="10" height="11" fill="none" stroke="#fff" stroke-width="1.5"/><path d="M7 10l1-3 6-6 2 2-6 6z" fill="#fff"/></symbol></defs></svg>
<div class="abs exp-col" style="left:242px;top:1282px">
  <div class="ex" style="top:0"><i><svg width="16" height="16"><use href="#edit"/></svg></i><span class="yr">2000-2005</span><h4>Lorem Ipsum Dolar</h4><p>Lorem ipsum dolor sit amet, consectetuer adipiscing elit, sed diam nonummy nibh euismod tincidunt ut laoreet dolore magna aliquam erat volutpat. Ut wisi enim ad minim veniam, quis nostrud</p></div>
  <div class="ex" style="top:177px"><i><svg width="16" height="16"><use href="#edit"/></svg></i><span class="yr">2007-2010</span><h4>Lorem Ipsum Dolar</h4><p>Lorem ipsum dolor sit amet, consectetuer adipiscing elit, sed diam nonummy nibh euismod tincidunt ut laoreet dolore magna aliquam erat volutpat. Ut wisi enim ad minim veniam, quis nostrud</p></div>
  <div class="ex" style="top:354px"><i><svg width="16" height="16"><use href="#edit"/></svg></i><span class="yr">2014-2020</span><h4>Lorem Ipsum Dolar</h4><p>Lorem ipsum dolor sit amet, consectetuer adipiscing elit, sed diam nonummy nibh euismod tincidunt ut laoreet dolore magna aliquam erat volutpat. Ut wisi enim ad minim veniam, quis nostrud</p></div>
</div>
<div class="abs exp-col" style="left:660px;top:1282px">
  <div class="ex" style="top:0"><i><svg width="16" height="16"><use href="#edit"/></svg></i><span class="yr">2005-2007</span><h4>Lorem Ipsum Dolar</h4><p>Lorem ipsum dolor sit amet, consectetuer adipiscing elit, sed diam nonummy nibh euismod tincidunt ut laoreet dolore magna aliquam erat volutpat. Ut wisi enim ad minim veniam, quis nostrud</p></div>
  <div class="ex" style="top:177px"><i><svg width="16" height="16"><use href="#edit"/></svg></i><span class="yr">2010-2014</span><h4>Lorem Ipsum Dolar</h4><p>Lorem ipsum dolor sit amet, consectetuer adipiscing elit, sed diam nonummy nibh euismod tincidunt ut laoreet dolore magna aliquam erat volutpat. Ut wisi enim ad minim veniam, quis nostrud</p></div>
  <div class="ex" style="top:354px"><i><svg width="16" height="16"><use href="#edit"/></svg></i><span class="yr">2020 till Continue</span><h4>Lorem Ipsum Dolar</h4><p>Lorem ipsum dolor sit amet, consectetuer adipiscing elit, sed diam nonummy nibh euismod tincidunt ut laoreet dolore magna aliquam erat volutpat. Ut wisi enim ad minim veniam, quis nostrud</p></div>
</div>

<div class="abs edu-band"></div>
<h2 class="abs edu-title">Education</h2>
<div class="card" style="left:163px"><div class="badge" role="img" aria-label="University crest"></div><span>2001 – 2004</span></div>
<div class="card" style="left:386px"><div class="badge" role="img" aria-label="College crest"></div><span>2004 – 2007</span></div>
<div class="card" style="left:610px"><div class="badge" role="img" aria-label="University crest"></div><span>2008 – 2009</span></div>
<div class="card" style="left:833px"><div class="badge" role="img" aria-label="State university crest"></div><span>2009 – 2010</span></div>

<h2 class="sec-title" style="top:2338px"><span>My Latest</span> Work</h2>
<div class="tile" style="left:48px;top:2427px;background:linear-gradient(135deg,#ffd21f,#f7b500)" role="img" aria-label="Under construction landing page mockup"></div>
<div class="tile" style="left:273px;top:2427px;background:linear-gradient(135deg,#e9e9e9,#cfd6e4)" role="img" aria-label="Digital marketing page mockup"></div>
<div class="tile" style="left:498px;top:2427px;background:linear-gradient(135deg,#fdc98a,#f59a52)" role="img" aria-label="Online shopping page mockup"></div>
<div class="tile" style="left:48px;top:2652px;background:linear-gradient(135deg,#8fe3cf,#4fcfb0)" role="img" aria-label="Pharmacy page mockup"></div>
<div class="tile" style="left:273px;top:2652px;background:linear-gradient(135deg,#dcdcdc,#1a3a46)" role="img" aria-label="Cryptocurrency landing page mockup"></div>
<div class="tile" style="left:498px;top:2652px;background:linear-gradient(135deg,#f4f4f4,#e6e6e6)" role="img" aria-label="Saving money page mockup"></div>
<div class="abs big" role="img" aria-label="Startup business landing page mockup"><div></div></div>
<div class="btn" style="left:541px;top:2894px;width:119px;height:44px">Contact Me</div>

<div class="abs blog-bg"></div>
<h2 class="sec-title" style="top:3114px"><span>My</span> Blog</h2>
<article class="post" style="left:163px;top:3204px;width:446px;height:420px">
  <div style="height:202px;background:linear-gradient(135deg,#2d84c2,#1a6aa8)" role="img" aria-label="Designer working at a desk"></div>
  <div style="padding:20px 22px">
    <h3>Lorem Ipsum Dolor Sit Amet Consectetuer Adipiscing</h3>
    <p style="margin-top:10px">sed diam nonummy nibh euismod tincid unt ut laoreet dolore magna aliqua erat volutpat nonummy nibh. sed diam nonummy nibh euismod tincid unt ut laoreet dolore magna sed diam nonummy nibh euismod tincid unt.</p>
    <div style="display:flex;justify-content:space-between;margin-top:28px;font-size:10px;color:#999"><span>By John Doe</span><span>• 04 month ago</span></div>
  </div>
</article>
<article class="post" style="left:631px;top:3204px;width:408px;height:199px;display:flex">
  <div style="width:173px;flex:none;background:linear-gradient(135deg,#e8e2d6,#f2c53a)" role="img" aria-label="Child drawing at a table"></div>
  <div style="padding:18px 24px"><h3>Lorem Ipsum Dolor Amet Consectet</h3><p style="margin-top:10px">sed diam nonummy nibh euismod tincid unt ut laoreet dolore magna aliquam erat volutpat nonummy nibh.</p></div>
</article>
<article class="post" style="left:631px;top:3425px;width:408px;height:199px;display:flex">
  <div style="width:173px;flex:none;background:linear-gradient(135deg,#cbb9a6,#b5a08c)" role="img" aria-label="Pushpins arranged on a board"></div>
  <div style="padding:18px 24px"><h3>Lorem Ipsum Dolor Amet Consectet</h3><p style="margin-top:10px">sed diam nonummy nibh euismod tincid unt ut laoreet dolore magna aliquam erat volutpat nonummy nonummy nibhnibh.</p></div>
</article>
<div class="btn" style="left:532px;top:3662px;width:135px;height:43px">View All Blogs</div>

<h2 class="sec-title" style="top:3882px"><span>Get In</span> Touch</h2>
<p class="abs contact-p">Lorem ipsum dolor sit amet, consectetuer adipiscing elit, sed diam nonummy nibh euismod tincidunt ut laoreet dolore magna aliquam erat volutpat. Ut wisi enim ad minim veniam, quis nostrud</p>
<div class="field" style="left:195px;top:4016px;width:457px;height:37px">Name</div>
<div class="field" style="left:195px;top:4065px;width:223px;height:36px">Email</div>
<div class="field" style="left:429px;top:4065px;width:223px;height:36px">Phone</div>
<div class="field" style="left:195px;top:4115px;width:457px;height:147px">Type your message here</div>
<div class="btn send">Send Message</div>
<div class="abs icard">
  <div class="irow" style="top:40px"><i><svg width="14" height="16" viewBox="0 0 14 16"><path d="M7 0a6 6 0 0 0-6 6c0 4 6 10 6 10s6-6 6-10a6 6 0 0 0-6-6z" fill="#6B429C"/><circle cx="7" cy="6" r="2" fill="#fff"/></svg></i><div><b>Daniel Reyes</b><br>123, Street, City<br>State XYZ 123 456</div></div>
  <div class="irow" style="top:145px"><i><svg width="14" height="14" viewBox="0 0 14 14"><path d="M3 1l2 3-1.5 1.5a8 8 0 0 0 5 5L10 9l3 2-1.5 2.5C6 13 1 8 .5 2.5z" fill="#6B429C"/></svg></i><div><b>Call Us On</b><br>123 456 7890</div></div>
  <div class="irow" style="top:230px"><i><svg width="16" height="12" viewBox="0 0 16 12"><rect width="16" height="12" rx="1" fill="#6B429C"/><path d="M1 1l7 6 7-6" fill="none" stroke="#fff" stroke-width="1.3"/></svg></i><div><b>Email Us On</b><br>hello@danielreyes.com</div></div>
</div>

<div class="abs foot-line"></div>
<p class="abs copy">Copyright © 2022 <b>Daniel Reyes.</b> All Rights Reserved.</p>
<div class="abs social"><i></i><i class="on"></i><i></i><i></i><i></i></div>

</body>
</html>
```